Velmora Water Purification

We need a website set up on a "Free account" WordPress platform. (This is the type of Wordpress site that you can sign up for and create online for free (not a server-hosted type.)
The website will be for a water purification company. They install devices in homes to purify the water for safer drinking, bathing, and cleaning.
Our logo is attached. Please keep color scheme of the website consistent with the logo.
Water Purification

```html
<!DOCTYPE html>
<html lang="en">
<head>
<meta charset="utf-8">
<title>Velmora Water Purification</title>
<link rel="stylesheet" href="https://fonts.googleapis.com/css2?family=Open+Sans:wght@400;600;700;800&display=swap">
<style>
:root{
  --page:#f6f8fb;
  --ink:#5b6670;
  --heading:#2b6db0;
  --deep:#2f6fb2;
  --band:#3f82c4;
  --band-light:#8fb8e0;
  --accent:#139fd3;
  --white:#ffffff;
  --photo-water:#cfe3f3;
  --photo-warm:#d9cfc4;
}
*{box-sizing:border-box;margin:0;padding:0}
html,body{width:1200px;height:3243px;overflow:hidden}
body{position:relative;background:var(--page);font-family:"Open Sans",Arial,sans-serif;color:var(--ink)}
.abs{position:absolute}
.btn{position:absolute;background:var(--accent);color:var(--white);font-weight:700;font-size:15px;text-transform:uppercase;display:flex;align-items:center;justify-content:center;letter-spacing:.3px}
.photo{position:absolute}

/* header */
.site-header{position:absolute;left:0;top:0;width:1200px;height:80px;background:var(--white)}
.brand{position:absolute;left:97px;top:30px;display:flex;align-items:center;gap:10px;font-weight:700;font-size:19px;color:var(--heading)}
.brand-dot{width:22px;height:22px;border-radius:50%;background:var(--accent)}
.main-nav{position:absolute;top:31px;left:728px;display:flex;gap:0;font-size:15px;font-weight:700;color:#333}
.main-nav span{position:absolute;white-space:nowrap}
.main-nav .current{color:var(--accent)}

/* hero */
.hero-bg{left:0;top:76px;width:1200px;height:482px;background:linear-gradient(90deg,#5b94cc,#d6e7f4 10%,#eaf3fa 50%,#d6e7f4 90%,#5b94cc)}
.hero-slide{left:97px;top:76px;width:1006px;height:480px;background:radial-gradient(ellipse at 62% 45%,#f4f9fd 0%,#cfe2f2 55%,#a9cbe8 100%)}
.hero-title{left:121px;top:225px;font-size:56px;font-weight:800;color:var(--deep);letter-spacing:-.5px}
.hero-sub{left:123px;top:294px;font-size:20px;font-weight:700;color:var(--deep);line-height:23px}
.slide-arrow{left:38px;top:282px;width:34px;height:34px;border-radius:50%;background:#4a5058}

/* why */
.why-title{left:636px;top:628px;font-size:30px;font-weight:600;color:var(--heading)}
.why-text{left:636px;top:680px;width:467px;font-size:12.5px;line-height:22.5px}
.why-text p{margin-bottom:12px}

/* bands */
.install-title{left:0;top:1100px;width:1200px;text-align:center;font-size:36px;font-weight:700;color:var(--white);line-height:49px}
.gallery-title{left:0;top:1433px;width:1200px;text-align:center;font-size:30px;font-weight:600;color:var(--heading)}
.round-arrow{width:34px;height:34px;border-radius:50%;background:var(--white);box-shadow:0 1px 4px rgba(0,0,0,.25)}
.exp-title{left:465px;top:1978px;font-size:35px;font-weight:600;color:var(--white);line-height:40px;text-transform:uppercase}
.exp-text{left:469px;top:2075px;width:640px;font-size:12px;line-height:22px;color:var(--white)}

/* blog */
.blog-title{left:0;top:2343px;width:1200px;text-align:center;font-size:30px;font-weight:600;color:var(--heading)}
.blog-lead{left:340px;top:2396px;width:520px;text-align:center;font-size:12px;line-height:22px}
.post-date{position:absolute;width:52px;height:80px;background:var(--accent);color:var(--white);font-size:21px;line-height:27px;text-align:center;padding-top:12px}
.post-title{position:absolute;font-size:17px;font-weight:700;color:var(--heading)}
.post-text{position:absolute;width:320px;font-size:11.5px;line-height:21px}
.post-more{position:absolute;font-size:11px;font-weight:700;color:var(--heading);text-transform:uppercase}

/* footer */
.foot-h{position:absolute;top:3010px;font-size:23px;color:var(--white)}
.foot-list{position:absolute;top:3044px;font-size:12px;line-height:26px;color:var(--white);list-style:none}
.foot-list svg{vertical-align:-2px;margin-right:6px}
.divider{position:absolute;top:3012px;width:1px;height:145px;background:rgba(255,255,255,.6)}
.email-box{left:493px;top:3053px;width:294px;height:41px;border:1px solid rgba(255,255,255,.8);font-size:12px;color:var(--white);padding:12px 14px}
.social{position:absolute;top:3057px;width:44px;height:44px;border-radius:50%;background:var(--white)}
.copyright{left:0;top:3214px;width:1200px;text-align:center;font-size:11px;color:var(--white)}
</style>
</head>
<body>

<header class="site-header">
  <div class="brand"><span class="brand-dot"></span>Velmora Water Purification</div>
  <nav class="main-nav">
    <span class="current" style="left:0">Home</span>
    <span style="left:70px">About</span>
    <span style="left:141px">Gallery</span>
    <span style="left:219px">Blog</span>
    <span style="left:277px">Contact</span>
    <span style="left:366px"><svg width="16" height="16" viewBox="0 0 16 16"><circle cx="6.5" cy="6.5" r="5" fill="none" stroke="#333" stroke-width="2"/><line x1="10" y1="10" x2="15" y2="15" stroke="#333" stroke-width="2"/></svg></span>
  </nav>
</header>

<section class="hero">
  <div class="abs hero-bg" role="img" aria-label="Water splash background"></div>
  <div class="photo hero-slide" role="img" aria-label="Glass of water splashing into clear water"></div>
  <div class="abs slide-arrow"><svg width="34" height="34" viewBox="0 0 34 34"><path d="M20 10 L12 17 L20 24" fill="none" stroke="#fff" stroke-width="3"/></svg></div>
  <h1 class="abs hero-title">Special Offer</h1>
  <p class="abs hero-sub">Call Now And get a Free Service<br>&nbsp;For 1 year</p>
  <a class="btn" style="left:121px;top:363px;width:143px;height:41px">Call Now</a>
</section>

<section class="why">
  <div class="photo" style="left:97px;top:638px;width:476px;height:292px;background:linear-gradient(135deg,#e9ecef,#b9c2c9 50%,#e2c9b4)" role="img" aria-label="Hand filling a glass from a kitchen tap"></div>
  <h2 class="abs why-title">Why Choose Us</h2>
  <div class="abs why-text">
    <p>Our certified technicians test your home water supply, recommend the right filter system and install it in a single visit. Every unit is sized for your household, so drinking, bathing and cleaning water stays clear, soft and safe all year long.</p>
    <p>We use proven multi-stage filtration that removes chlorine, sediment and heavy metals while keeping healthy minerals. Regular service visits, free replacement parts in the first year and friendly local support keep your system running.</p>
  </div>
  <a class="btn" style="left:636px;top:893px;width:114px;height:37px;font-size:13px">Read More</a>
</section>

<section class="install">
  <svg class="abs" style="left:0;top:995px" width="1200" height="395" viewBox="0 0 1200 395">
    <defs><linearGradient id="installFill" x1="0" y1="0" x2="0" y2="1"><stop offset="0" stop-color="#2f72b8"/><stop offset="1" stop-color="#5d97d0"/></linearGradient></defs>
    <path d="M0 10 C300 -10 500 60 800 40 C1000 25 1120 5 1200 0 L1200 360 C1000 395 800 350 600 370 C380 392 200 350 0 375 Z" fill="url(#installFill)" role="img" aria-label="Blue water texture band"/>
  </svg>
  <h2 class="abs install-title">We Install devices in homes to purify the water for<br>safer drinking, bathing, and cleaning</h2>
  <a class="btn" style="left:532px;top:1232px;width:145px;height:44px;font-size:14px">Book Now</a>
</section>

<section class="gallery">
  <h2 class="abs gallery-title">Gallery</h2>
  <div class="photo" style="left:97px;top:1509px;width:327px;height:193px;background:linear-gradient(135deg,#cfd3d6,#9aa3a8 60%,#d8c6b2)" role="img" aria-label="Under-sink water filter filling a glass"></div>
  <div class="photo" style="left:437px;top:1509px;width:326px;height:193px;background:linear-gradient(135deg,#eef2f4,#d8c3b1 55%,#b8d4ea)" role="img" aria-label="Woman splashing clean water"></div>
  <div class="photo" style="left:776px;top:1509px;width:327px;height:193px;background:linear-gradient(135deg,#e6e8ea,#c9cdd0 50%,#a8c46e)" role="img" aria-label="Filter jug and fresh vegetables in a kitchen"></div>
  <div class="abs round-arrow" style="left:1112px;top:1665px"><svg width="34" height="34" viewBox="0 0 34 34"><path d="M19 12 L14 17 L19 22" fill="none" stroke="#333" stroke-width="2"/></svg></div>
  <div class="abs round-arrow" style="left:1155px;top:1665px"><svg width="34" height="34" viewBox="0 0 34 34"><path d="M15 12 L20 17 L15 22" fill="none" stroke="#333" stroke-width="2"/></svg></div>
</section>

<section class="experience">
  <svg class="abs" style="left:0;top:1790px" width="1200" height="510" viewBox="0 0 1200 510">
    <defs><linearGradient id="expFill" x1="0" y1="0" x2="0" y2="1"><stop offset="0" stop-color="#d2e3f2"/><stop offset=".45" stop-color="#8db5dc"/><stop offset="1" stop-color="#4f88c4"/></linearGradient></defs>
    <path d="M0 30 C250 80 520 70 760 45 C980 20 1100 5 1200 12 L1200 470 C1000 500 800 430 560 455 C330 480 150 500 0 455 Z" fill="url(#expFill)" role="img" aria-label="Soft water bubbles background"/>
  </svg>
  <div class="abs" style="left:93px;top:1918px;width:302px;height:302px;border-radius:50%;background:var(--accent)"></div>
  <div class="photo" style="left:103px;top:1928px;width:282px;height:282px;border-radius:50%;background:radial-gradient(circle at 50% 40%,#e8d2c0,#b48c6a 60%,#6f8fab)" role="img" aria-label="Young girl drinking a glass of water"></div>
  <h2 class="abs exp-title">With over 10 years of experience<br>in the water filter market</h2>
  <p class="abs exp-text">Lorem Ipsum is simply dummy text of the printing and typesetting industry. Lorem Ipsum has been the industry's standard dummy text ever since the 1500s.</p>
  <a class="btn" style="left:469px;top:2145px;width:108px;height:39px;font-size:13px">Read More</a>
</section>

<section class="blog">
  <h2 class="abs blog-title">Our Blog</h2>
  <p class="abs blog-lead">Organically grow the holistic world view of disruptive innovation via workplace diversity and empowerment.</p>

  <article>
    <div class="photo" style="left:99px;top:2482px;width:320px;height:227px;background:linear-gradient(135deg,#f0e3d8,#dcb9a0 60%,#c9d6e0)" role="img" aria-label="Baby being bathed in clean water"></div>
    <div class="abs" style="left:112px;top:2492px"><svg width="22" height="30" viewBox="0 0 22 30"><circle cx="11" cy="10" r="8" fill="#139fd3"/><line x1="11" y1="18" x2="11" y2="29" stroke="#139fd3" stroke-width="2"/></svg></div>
    <div class="post-date" style="left:367px;top:2482px">08<br>Nov</div>
    <h3 class="post-title" style="left:99px;top:2732px">Lorem Ipsum Is Simply Dummy</h3>
    <p class="post-text" style="left:99px;top:2764px">Lorem Ipsum is simply dummy text of the printing . It is tLorem Ipsum has been the industry's standard dummy text ever since the 1500s.</p>
    <span class="post-more" style="left:99px;top:2837px">Read More</span>
  </article>

  <article>
    <div class="photo" style="left:437px;top:2482px;width:324px;height:227px;background:linear-gradient(135deg,#d8d2c8,#b7a593 55%,#8fa8bf)" role="img" aria-label="Boy drinking a glass of water"></div>
    <div class="post-date" style="left:709px;top:2482px">10<br>Nov</div>
    <h3 class="post-title" style="left:440px;top:2732px">Lorem Ipsum Is Simply Dummy</h3>
    <p class="post-text" style="left:440px;top:2764px">Lorem Ipsum is simply dummy text of the printing . It is tLorem Ipsum has been the industry's standard dummy text ever since the 1500s.</p>
    <span class="post-more" style="left:440px;top:2837px">Read More</span>
  </article>

  <article>
    <div class="photo" style="left:780px;top:2482px;width:323px;height:227px;background:linear-gradient(135deg,#e4e6e2,#c9b49a 50%,#d0463a)" role="img" aria-label="Washing fresh peppers under a tap"></div>
    <div class="post-date" style="left:1051px;top:2482px">14<br>Nov</div>
    <h3 class="post-title" style="left:782px;top:2732px">Lorem Ipsum Is Simply Dummy</h3>
    <p class="post-text" style="left:782px;top:2764px">Lorem Ipsum is simply dummy text of the printing . It is tLorem Ipsum has been the industry's standard dummy text ever since the 1500s.</p>
    <span class="post-more" style="left:782px;top:2837px">Read More</span>
  </article>
</section>

<footer class="site-footer">
  <svg class="abs" style="left:0;top:2900px" width="1200" height="343" viewBox="0 0 1200 343">
    <defs><linearGradient id="footFill" x1="0" y1="0" x2="0" y2="1"><stop offset="0" stop-color="#2c6db4"/><stop offset=".4" stop-color="#4a86c6"/><stop offset="1" stop-color="#5a93cd"/></linearGradient></defs>
    <path d="M0 20 C250 5 500 40 750 25 C950 12 1100 0 1200 8 L1200 343 L0 343 Z" fill="url(#footFill)" role="img" aria-label="Water surface footer background"/>
  </svg>

  <h4 class="foot-h" style="left:97px">About</h4>
  <ul class="foot-list" style="left:97px"><li>Responsibility</li><li>Awards</li><li>History</li><li>News</li></ul>
  <div class="divider" style="left:218px"></div>

  <h4 class="foot-h" style="left:257px">Contact Us</h4>
  <ul class="foot-list" style="left:260px">
    <li><svg width="10" height="13" viewBox="0 0 10 13"><path d="M5 0 A5 5 0 0 1 10 5 C10 8 5 13 5 13 C5 13 0 8 0 5 A5 5 0 0 1 5 0Z" fill="#fff"/></svg>Map &amp; Directions</li>
    <li><svg width="12" height="11" viewBox="0 0 12 11"><path d="M0 5 L12 0 L9 11 L6 7 Z" fill="#fff"/></svg>Send A Message</li>
    <li><svg width="12" height="9" viewBox="0 0 12 9"><rect width="12" height="9" fill="#fff"/><path d="M0 0 L6 5 L12 0" fill="none" stroke="#4a86c6"/></svg>Email Us</li>
    <li><svg width="11" height="11" viewBox="0 0 11 11"><path d="M2 0 L4 3 L3 4 C4 6 5 7 7 8 L8 7 L11 9 L9 11 C4 10 1 7 0 2 Z" fill="#fff"/></svg>Call Us 1-800-555-0142</li>
  </ul>
  <div class="divider" style="left:447px"></div>

  <h4 class="foot-h" style="left:493px">Subscribe Newsletter</h4>
  <div class="abs email-box">Enter Your Email
    <svg style="position:absolute;right:14px;top:15px" width="13" height="10" viewBox="0 0 13 10"><rect width="13" height="10" fill="#fff"/><path d="M0 0 L6.5 5 L13 0" fill="none" stroke="#4a86c6"/></svg>
  </div>
  <a class="btn" style="left:493px;top:3111px;width:99px;height:26px;font-size:11px">Subscribe</a>
  <div class="divider" style="left:832px"></div>

  <h4 class="foot-h" style="left:867px">Follow Us</h4>
  <span class="social" style="left:869px" aria-label="Social profile"></span>
  <span class="social" style="left:931px" aria-label="Social profile"></span>
  <span class="social" style="left:994px" aria-label="Social profile"></span>
  <span class="social" style="left:1057px" aria-label="Social profile"></span>

  <div class="abs" style="left:97px;top:3203px;width:1006px;height:1px;background:rgba(255,255,255,.5)"></div>
  <p class="abs copyright">Copyright © 2017 Velmora Water Purification. All Rights Reserved.</p>
</footer>

</body>
</html>
```